Brocure for Brisval - Social Media Management

Brisval is a Dutch company in the market of Social Media growth. We need a brochure (digital/PDF) for our company. Please see attached word doc for the text and attached logo. The initial proposal can contain just the first 4 pages text of the word doc.

We use informal language in all our communication.

Slogan: Effectieve Social Media Marketing voor professionals en ondernemers

Website: brisvalsm.nl

Industry/Entity Type

Digital Marketing

Contact Information for Business Card

Contact details:

Jorrit ter Meulen
jorrit@brisvalsm.nl
06-47195362

```html
<!DOCTYPE html>
<html lang="nl">
<head>
<meta charset="utf-8">
<title>Brisval – Social Media Management brochure</title>
<link href="https://fonts.googleapis.com/css2?family=Poppins:wght@400;600;700;800&family=Open+Sans:wght@400;600;700&display=swap" rel="stylesheet">
<style>
:root{
  --bg:#e9f2fb;
  --page:#ffffff;
  --orange:#f26a1b;
  --orange-soft:#fbd2b4;
  --blue:#27a3d9;
  --blue-dark:#1b6fa8;
  --navy:#1f2a44;
  --text:#4a5160;
  --muted:#8b919c;
  --line:#e3e6ea;
}
*{box-sizing:border-box;margin:0;padding:0}
html,body{width:1200px;height:4568px;overflow:hidden;background:var(--bg)}
body{position:relative;font-family:"Open Sans",Arial,sans-serif;color:var(--text)}
.page{position:absolute;left:48px;width:1104px;background:var(--page);box-shadow:0 6px 24px rgba(31,42,68,.10);overflow:hidden}
.page-footer{position:absolute;left:60px;right:60px;bottom:28px;display:flex;justify-content:space-between;font-size:13px;color:var(--muted);padding-top:10px;border-top:3px solid var(--orange)}
.page-footer .site{color:var(--orange);font-weight:600}
.art{position:absolute;border-radius:12px}
h1,h2,h3{font-family:"Poppins",Arial,sans-serif}
p{font-size:14px;line-height:1.6}

/* page 1 */
.cover{top:20px;height:900px}
.cover .art{left:332px;top:60px;width:440px;height:360px;border-radius:50% 46% 50% 44%;background:radial-gradient(circle at 50% 45%,#f58a44 0,#fbc9a4 55%,#fde9db 75%,#fff 100%)}
.cover h1{position:absolute;top:470px;left:0;right:0;text-align:center;color:var(--orange);font-size:34px;font-weight:700;line-height:1.25}
.cover .kicker{position:absolute;top:570px;left:0;right:0;text-align:center;font-family:"Poppins",sans-serif;font-weight:600;font-size:14px;letter-spacing:1px;color:var(--navy)}
.cover .rule{position:absolute;top:600px;left:502px;width:100px;height:2px;background:var(--orange)}
.cover .intro{position:absolute;top:630px;left:250px;width:604px;text-align:center}
.cover .formula{position:absolute;top:755px;left:0;right:0;text-align:center;color:var(--orange);font-family:"Poppins",sans-serif;font-weight:700;font-size:22px}

/* page 2 */
.about{top:980px;height:850px}
.about .phone-art{left:70px;top:40px;width:250px;height:220px;background:linear-gradient(135deg,#f7a46f,#2b3a5c)}
.section-title{font-size:30px;font-weight:800;color:var(--navy);line-height:1.1}
.about .who{position:absolute;left:380px;top:60px;width:660px}
.about .who p{margin-top:14px}
.about .who .tag{color:var(--orange);font-style:italic;font-weight:600}
.about .band{position:absolute;left:0;right:0;top:295px;height:150px;background:var(--orange)}
.about .band h2{position:absolute;left:60px;top:20px;color:#fff;font-size:30px;font-weight:800}
.about .band p{position:absolute;left:60px;top:72px;width:520px;color:#fff}
.about .qmarks{position:absolute;right:120px;top:-10px;font-family:"Poppins",sans-serif;font-weight:800;font-size:120px;color:#fff;line-height:1}
.about .qmarks span{display:inline-block;width:90px;height:110px;border-radius:50%;background:#fff}
.about .plant-art{left:70px;top:480px;width:250px;height:240px;background:linear-gradient(160deg,#f9c04a,#5dab4f 60%,#2b3a5c)}
.about .what{position:absolute;left:380px;top:480px;width:660px}
.about .what p{margin-top:12px}

/* page 3 */
.platforms{top:1880px;height:880px}
.platforms .banner{position:absolute;left:0;right:0;top:40px;height:400px;background:linear-gradient(120deg,var(--blue) 0,#3cc0ea 100%)}
.platforms .banner-tab{position:absolute;left:0;top:30px;background:var(--navy);color:#fff;font-family:"Poppins",sans-serif;font-weight:700;font-size:22px;padding:12px 40px 12px 60px;border-radius:0 30px 30px 0}
.platforms .banner-lead{position:absolute;left:60px;top:100px;color:#fff;font-weight:700;font-size:14px;line-height:1.35;text-transform:uppercase}
.platforms ul{position:absolute;left:60px;top:150px;list-style:none}
.platforms li{display:flex;align-items:center;gap:10px;color:#fff;font-size:14px;margin-bottom:13px}
.platforms .laptop-art{left:560px;top:60px;width:480px;height:300px;background:linear-gradient(135deg,#1f4f8a,#4fd0f0 60%,#f4a25a)}
.platforms .names{position:absolute;left:60px;right:60px;top:470px;display:flex;flex-wrap:wrap;justify-content:center;gap:22px 60px;font-family:"Poppins",sans-serif;font-weight:700;font-size:24px;color:var(--navy)}
.platforms .divider{position:absolute;left:60px;right:60px;top:600px;height:1px;background:var(--line)}
.platforms .why{position:absolute;left:60px;top:640px;width:300px}
.platforms .brand{display:flex;align-items:center;gap:10px;margin-top:16px;font-family:"Poppins",sans-serif;font-weight:700;font-size:24px;color:var(--orange)}
.platforms .brand i{width:30px;height:30px;border-radius:50%;background:var(--orange)}
.platforms .why-text{position:absolute;left:460px;top:640px;width:580px}
.platforms .why-text p+p{margin-top:10px}

/* page 4 */
.details{top:2840px;height:940px}
.details .col{position:absolute;left:60px;top:50px;width:560px}
.details h3{color:var(--orange);font-size:13px;font-weight:700;text-transform:uppercase;margin:16px 0 4px}
.details p{font-size:12.5px;line-height:1.55}
.details .people-art{left:650px;top:240px;width:400px;height:400px;background:linear-gradient(160deg,#f0f0f0,#c9ced6 50%,#f5b48a)}

/* page 5 */
.steps{top:3840px;height:700px}
.steps h2{position:absolute;left:60px;top:40px;font-size:28px;font-weight:700;color:var(--navy)}
.steps .track{position:absolute;left:0;top:0}
.step{position:absolute;left:150px;width:560px}
.step h4{font-family:"Poppins",sans-serif;color:var(--orange);font-size:16px;font-weight:700}
.step p{font-size:12.5px;margin-top:4px}
.step-icon{position:absolute;left:860px;width:90px;height:90px;border-radius:50%;background:#fff;border:3px solid var(--orange);display:flex;align-items:center;justify-content:center}
</style>
</head>
<body>

<section class="page cover">
  <div class="art" role="img" aria-label="Illustratie: oranje gloeilamp omringd door social media pictogrammen"></div>
  <h1>Social Media Marketing voor zakelijke<br>professionals en ondernemers</h1>
  <div class="kicker">SNELLE INTRODUCTIE EN OVERZICHT</div>
  <div class="rule"></div>
  <p class="intro">Je bereikt meer mensen, trekt gericht de juiste klanten aan en bouwt aan je merk. Dat is social media in een notendop.<br><br>Zo werkt het: betere interactie en relevante content zorgen voor actieve volgers, en die leveren meer traffic en sales op.</p>
  <div class="formula">((betere interactie + relevante content) × actieve volgers) = (+ traffic + sales)</div>
  <footer class="page-footer"><span>Brisval – Social Media Management</span><span class="site">www.brisvalsm.nl</span></footer>
</section>

<section class="page about">
  <div class="art phone-art" role="img" aria-label="Illustratie: hand met smartphone en megafoon"></div>
  <div class="who">
    <h2 class="section-title">WIE ZIJN WIJ?</h2>
    <p><strong>Wij zijn Brisval</strong>, een team van social media experts dat ondernemers helpt om online zichtbaar te worden. We zorgen voor content die bij je past en voor volgers die echt iets met je merk hebben.</p>
    <p>We houden het persoonlijk en informeel, want zo werkt social media nu eenmaal het best.</p>
    <p class="tag">Wij doen het werk, jij kunt ondernemen!</p>
  </div>
  <div class="band">
    <h2>VOOR WIE?</h2>
    <p>Voor zakelijke professionals en ondernemers die meer uit social media willen halen, maar daar zelf geen tijd of zin in hebben.</p>
    <div class="qmarks">??</div>
  </div>
  <div class="art plant-art" role="img" aria-label="Illustratie: groeiende plant met zon en munten"></div>
  <div class="what">
    <h2 class="section-title">WAT DOEN WE?</h2>
    <p>Samen met jou bepalen we je doelen en je ideale doelgroep. Daarna maken we een plan met de juiste kanalen, berichten en timing.</p>
    <p>We zorgen voor content die aanslaat: posts, stories, video's en advertenties. Alles afgestemd op jouw merk en je eigen stijl.</p>
    <p>Ook reageren we op berichten en bouwen we actief aan een community rond je bedrijf. Zo groeien je bereik en je volgers stap voor stap.</p>
    <p>Elke maand krijg je een heldere rapportage, zodat je precies ziet wat het oplevert en waar we nog kunnen verbeteren.</p>
  </div>
  <footer class="page-footer"><span>Brisval – Social Media Management</span><span class="site">www.brisvalsm.nl</span></footer>
</section>

<section class="page platforms">
  <div class="banner">
    <div class="banner-tab">Welke platformen?</div>
    <div class="banner-lead">We kunnen jouw bedrijf laten groeien<br>op alle grote platformen</div>
    <ul>
      <li><svg width="18" height="18" viewBox="0 0 18 18"><circle cx="9" cy="9" r="9" fill="#fff"/><path d="M5 9.5l2.6 2.5L13 6.5" stroke="#27a3d9" stroke-width="2" fill="none"/></svg>Netwerkly: zakelijk netwerken en leads</li>
      <li><svg width="18" height="18" viewBox="0 0 18 18"><circle cx="9" cy="9" r="9" fill="#fff"/><path d="M5 9.5l2.6 2.5L13 6.5" stroke="#27a3d9" stroke-width="2" fill="none"/></svg>Vriendbook: community en advertenties</li>
      <li><svg width="18" height="18" viewBox="0 0 18 18"><circle cx="9" cy="9" r="9" fill="#fff"/><path d="M5 9.5l2.6 2.5L13 6.5" stroke="#27a3d9" stroke-width="2" fill="none"/></svg>Plaatjr: beeld, stories en reels</li>
      <li><svg width="18" height="18" viewBox="0 0 18 18"><circle cx="9" cy="9" r="9" fill="#fff"/><path d="M5 9.5l2.6 2.5L13 6.5" stroke="#27a3d9" stroke-width="2" fill="none"/></svg>Tjilp</li>
      <li><svg width="18" height="18" viewBox="0 0 18 18"><circle cx="9" cy="9" r="9" fill="#fff"/><path d="M5 9.5l2.6 2.5L13 6.5" stroke="#27a3d9" stroke-width="2" fill="none"/></svg>Kijktube</li>
      <li><svg width="18" height="18" viewBox="0 0 18 18"><circle cx="9" cy="9" r="9" fill="#fff"/><path d="M5 9.5l2.6 2.5L13 6.5" stroke="#27a3d9" stroke-width="2" fill="none"/></svg>Zoekr Bedrijfsprofiel</li>
      <li><svg width="18" height="18" viewBox="0 0 18 18"><circle cx="9" cy="9" r="9" fill="#fff"/><path d="M5 9.5l2.6 2.5L13 6.5" stroke="#27a3d9" stroke-width="2" fill="none"/></svg>Klipklap, Prikbord en meer</li>
    </ul>
    <div class="art laptop-art" role="img" aria-label="Illustratie: laptop met video, grafieken en raket"></div>
  </div>
  <div class="names">
    <span>Netwerkly</span><span>Vriendbook</span><span>Plaatjr</span><span>Tjilp</span><span>Kijktube</span><span>Zoekr</span>
  </div>
  <div class="divider"></div>
  <div class="why">
    <h2 class="section-title">WAAROM KIES<br>JE VOOR</h2>
    <div class="brand"><i></i>Brisval</div>
  </div>
  <div class="why-text">
    <p>Je wilt groei zien, geen vage beloftes. Wij werken met duidelijke doelen en laten elke maand zien wat we hebben bereikt.</p>
    <p>We kennen de platformen door en door en weten wat werkt voor jouw branche. Zo haal je meer uit je tijd en budget.</p>
    <p>En het belangrijkste: je hebt één vast aanspreekpunt dat jouw bedrijf echt kent en met je meedenkt.</p>
  </div>
  <footer class="page-footer"><span>Brisval – Social Media Management</span><span class="site">www.brisvalsm.nl</span></footer>
</section>

<section class="page details">
  <div class="col">
    <h3>Persoonlijk advies</h3>
    <p>We starten met een kennismaking. Daarin bespreken we je doelen, je doelgroep en waar je nu staat. Zo weten we precies waar we moeten beginnen.</p>
    <p>Je krijgt een plan op maat, zonder onnodige poespas.</p>
    <h3>Strategie die bij je past</h3>
    <p>Geen standaardpakket, maar een aanpak die aansluit op jouw bedrijf. We kiezen de kanalen waar jouw klanten zitten en bepalen welke content daar het best werkt.</p>
    <h3>Content die opvalt</h3>
    <p>We maken berichten, visuals en video's die aandacht trekken en aanzetten tot actie. Alles in jouw stijl en toon, zodat het herkenbaar blijft voor je volgers.</p>
    <h3>Community en interactie</h3>
    <p>Social media draait om contact. We reageren op vragen en berichten, gaan het gesprek aan en zorgen dat je volgers zich betrokken voelen bij je merk.</p>
    <h3>Gerichte advertenties</h3>
    <p>Met slimme campagnes bereik je precies de mensen die je zoekt. We testen, meten en sturen bij, zodat elke euro zo veel mogelijk oplevert.</p>
    <h3>Heldere rapportages</h3>
    <p>Elke maand krijg je een overzicht van bereik, interactie, groei en resultaten. Zo zie je in één oogopslag wat het oplevert.</p>
    <h3>Samen verder groeien</h3>
    <p>We evalueren regelmatig en passen het plan aan waar dat nodig is. Zo blijf je groeien, ook als je markt of doelen veranderen.</p>
  </div>
  <div class="art people-art" role="img" aria-label="Illustratie: team met laptops, grafieken en groeipijl"></div>
  <footer class="page-footer"><span>Brisval – Social Media Management</span><span class="site">www.brisvalsm.nl</span></footer>
</section>

<section class="page steps">
  <h2>Hoe werkt het?</h2>
  <svg class="track" width="1104" height="700" viewBox="0 0 1104 700" aria-hidden="true">
    <path d="M100 120 V590" stroke="#f26a1b" stroke-width="2" stroke-dasharray="6 6" fill="none"/>
    <path d="M905 120 C1000 160,1000 220,905 230 C1000 270,1000 330,905 340 C1000 380,1000 440,905 450 C1000 490,1000 550,905 560" stroke="#fbd2b4" stroke-width="3" fill="none"/>
    <g fill="#f26a1b"><circle cx="100" cy="120" r="9"/><circle cx="100" cy="230" r="9"/><circle cx="100" cy="340" r="9"/><circle cx="100" cy="450" r="9"/><circle cx="100" cy="560" r="9"/></g>
  </svg>
  <div class="step" style="top:100px"><h4>Quick Scan &amp; intake</h4><p>We bekijken waar je nu staat en bespreken je doelen. Zo weten we precies wat er nodig is om te groeien.</p></div>
  <div class="step" style="top:210px"><h4>Je stelt zelf wie je wilt</h4><p>Samen bepalen we wie je wilt bereiken en welke kanalen daarbij passen. Jij houdt de regie over je merk.</p></div>
  <div class="step" style="top:320px"><h4>Plan en content</h4><p>We maken een contentplan en gaan aan de slag met posts, visuals en advertenties die bij je passen.</p></div>
  <div class="step" style="top:430px"><h4>Uitvoeren en bijsturen</h4><p>We plaatsen, reageren en meten. Wat goed werkt doen we vaker, wat minder werkt passen we aan.</p></div>
  <div class="step" style="top:540px"><h4>Terugkoppeling en verbetering</h4><p>Elke maand krijg je een rapport en bespreken we samen de volgende stappen om verder te groeien.</p></div>
  <div class="step-icon" style="top:75px"><svg width="40" height="40" viewBox="0 0 40 40"><circle cx="17" cy="17" r="10" stroke="#f26a1b" stroke-width="3" fill="none"/><path d="M25 25l9 9" stroke="#f26a1b" stroke-width="3"/></svg></div>
  <div class="step-icon" style="top:185px"><svg width="40" height="40" viewBox="0 0 40 40"><circle cx="20" cy="20" r="14" stroke="#f26a1b" stroke-width="3" fill="none"/><circle cx="20" cy="20" r="5" fill="#f26a1b"/></svg></div>
  <div class="step-icon" style="top:295px"><svg width="40" height="40" viewBox="0 0 40 40"><rect x="8" y="6" width="24" height="28" rx="3" stroke="#f26a1b" stroke-width="3" fill="none"/><path d="M13 15h14M13 21h14M13 27h9" stroke="#f26a1b" stroke-width="2"/></svg></div>
  <div class="step-icon" style="top:405px"><svg width="40" height="40" viewBox="0 0 40 40"><path d="M6 32h28M10 32V22M18 32V14M26 32V18" stroke="#f26a1b" stroke-width="4"/></svg></div>
  <div class="step-icon" style="top:515px"><svg width="40" height="40" viewBox="0 0 40 40"><path d="M8 21l8 8L32 11" stroke="#f26a1b" stroke-width="4" fill="none"/></svg></div>
  <footer class="page-footer"><span>Brisval – Social Media Management</span><span class="site">www.brisvalsm.nl</span></footer>
</section>

</body>
</html>
```